Computer repair services flyer

This flyer / leaflet is required to promote my local computer and laptop repair business. It will primarily be used for pinning to notice boards when I get access to shared accommodation but I will also use it in the future for posting through letterboxes in affluent areas.

Company branding, logo, services, pricing, contact details etc. can be found on my website at : www.brightlanetech.co.uk

The services I would predominantly like to promote on this flyer are :

Speeding up slow / old computers
Virus removal
Lost data recovered
Broken laptop screen replacements
Dead laptops fixed
We buy and recycle broken laptops for cash

Other features to highlight :

Friendly and experienced
We are local (Near to Cardiff city center)
Quick repair turnaround - most repairs within 24hours
Affordable / No VAT
Free diagnostics
No Fix = No fee
Free collection and delivery
We Guarantee our work

Calls to action and attention grabbing if possible. Offer 10% off. Free cooling fan clean.

Size of flyer = A5 (210 x 148mm or 8.3 x 5.8in) portrait, single sided colour.

Target Market(s)

18 to 60 years

Industry/Entity Type

Accommodation

Requirements
Must have
• 02940 613857

```html
<!DOCTYPE html>
<html lang="en">
<head>
<meta charset="utf-8">
<title>Bright Lane Tech – Computer Repair Flyer</title>
<link rel="stylesheet" href="https://fonts.googleapis.com/css2?family=Roboto+Condensed:wght@400;700;800&display=swap">
<style>
  :root {
    --orange: #f47b20;
    --orange-deep: #e0600c;
    --orange-light: #ffa04a;
    --ink: #2b2b2b;
    --paper: #ffffff;
    --paper-shade: #eef0f2;
    --photo-light: #dfe8ef;
    --photo-mid: #9fb4c4;
    --photo-dark: #3f5668;
  }
  * { box-sizing: border-box; margin: 0; padding: 0; }
  html, body { width: 847px; height: 1200px; overflow: hidden; background: var(--paper); }
  .flyer {
    position: relative; width: 847px; height: 1200px; overflow: hidden;
    background: linear-gradient(180deg, var(--paper) 0%, var(--paper) 55%, var(--paper-shade) 100%);
    font-family: "Roboto Condensed", "Arial Narrow", sans-serif; color: var(--ink);
  }

  /* Header */
  .brand {
    position: absolute; left: 34px; top: 40px;
    display: flex; align-items: center; gap: 16px;
  }
  .brand-dot { width: 46px; height: 46px; border-radius: 50%; background: var(--orange); }
  .brand-name {
    font-weight: 800; font-size: 66px; line-height: 1; color: var(--orange); letter-spacing: -1px;
  }
  .brand-tag {
    position: absolute; left: 96px; top: 118px;
    font-size: 30px; font-weight: 400; color: var(--ink);
  }
  .contact {
    position: absolute; right: 30px; top: 44px; text-align: right;
    font-weight: 700; color: var(--orange); font-size: 36px; line-height: 1.2;
  }

  /* Offer banner */
  .offer {
    position: absolute; left: 0; top: 192px; width: 847px; height: 128px;
    background: linear-gradient(180deg, var(--orange-light) 0%, var(--orange) 45%, var(--orange-deep) 100%);
    color: var(--paper); text-align: center; padding-top: 14px;
  }
  .offer-line { font-weight: 700; font-size: 46px; line-height: 1.15; }
  .offer-line .big { font-size: 58px; font-weight: 800; }
  .offer-sub { font-weight: 700; font-size: 42px; line-height: 1.15; }

  /* Feature badges */
  .badge {
    position: absolute; border-radius: 50%;
    background: radial-gradient(circle at 35% 30%, var(--orange-light), var(--orange) 55%, var(--orange-deep));
    color: var(--paper); font-weight: 700; display: flex; align-items: center; justify-content: center;
  }
  .badge-fast { left: 22px; top: 382px; width: 112px; height: 112px; font-size: 40px; }
  .badge-free { left: 22px; top: 508px; width: 112px; height: 112px; font-size: 40px; }
  .badge-repair { left: 530px; top: 612px; width: 118px; height: 118px; font-size: 36px; }

  .feature { position: absolute; font-weight: 700; color: var(--ink); line-height: 1.15; }
  .feature-fast { left: 150px; top: 385px; width: 290px; font-size: 27px; }
  .feature-fast .accent { font-size: 42px; }
  .feature-free { left: 150px; top: 520px; font-size: 30px; }
  .feature-free .accent { font-size: 38px; }

  .local {
    position: absolute; left: 462px; top: 398px; width: 375px;
    color: var(--orange); font-weight: 700; font-size: 30px; line-height: 1.25;
  }

  /* Photo area */
  .photo {
    position: absolute; left: 0; top: 640px; width: 560px; height: 458px;
    background: linear-gradient(160deg, var(--photo-light) 0%, var(--photo-mid) 55%, var(--photo-dark) 100%);
    clip-path: polygon(6% 4%, 84% 0%, 92% 78%, 100% 100%, 0% 100%, 0% 8%);
  }

  /* Services */
  .services {
    position: absolute; left: 575px; top: 735px; width: 260px;
    list-style: none; text-align: center;
    font-weight: 700; font-size: 27px; line-height: 1.22; color: var(--ink);
  }

  /* Footer */
  .guarantee {
    position: absolute; left: 0; bottom: 0; width: 847px; height: 102px;
    background: linear-gradient(180deg, var(--orange-light) 0%, var(--orange) 40%, var(--orange-deep) 100%);
    color: var(--paper); font-weight: 700; font-size: 42px;
    display: flex; align-items: center; justify-content: center;
  }
</style>
</head>
<body>
<main class="flyer">
  <header>
    <div class="brand">
      <span class="brand-dot"></span>
      <span class="brand-name">Bright Lane Tech</span>
    </div>
    <p class="brand-tag">and your laptop too!</p>
    <div class="contact">
      <p>Call Now</p>
      <p>02940 613857</p>
      <p>No Fix = No Fee</p>
    </div>
  </header>

  <section class="offer">
    <p class="offer-line">Calls to action !! Offer <span class="big">10%</span> off</p>
    <p class="offer-sub">Free cooling fan clean</p>
  </section>

  <div class="badge badge-fast">Fast</div>
  <p class="feature feature-fast">Quick repair turnaround<br>Most repairs within<br><span class="accent">24hours</span></p>

  <p class="local">Friendly and experienced<br>We are local near to Cardiff<br>city center</p>

  <div class="badge badge-free">Free</div>
  <p class="feature feature-free">Affordable / No VAT<br><span class="accent">Free</span> diagnostics · <span class="accent">Free</span> collection and delivery</p>

  <div class="photo" role="img" aria-label="Open laptop with a doctor's hand holding a stethoscope to the screen"></div>

  <div class="badge badge-repair">Repair</div>
  <ul class="services">
    <li>Speeding up slow / old computers</li>
    <li>Virus removal</li>
    <li>Lost data recovered</li>
    <li>Broken laptop screen replacements</li>
    <li>Dead laptops fixed</li>
    <li>Buy and recycle broken laptops for cash</li>
  </ul>

  <footer class="guarantee">We Guarantee our work</footer>
</main>
</body>
</html>
```